Sign Shop website

We need a web design for a sign company called Quillby Signs that builds signs for shops such as A Frames, Banners, Tennet Boards, Shop front windows etc...

The existing site is avaliable at www.quillbysigns.com.au

We will need to have a fresh makeover. The new site must have the following:

Photo Galleries (broken down into sections)
Store Locations (currently there are 4 stores)
Online quote form
List of services
About Us Page

We just need to front page designed in photoshop (the inner page is not necessary) We have a team that can code the site up.

The website should have the exact logo. Any person who alters the logo, design will be elimated.

No Twitter, RSS, LinkedIn icons

The main colours are yellow, black, blue, red

Target Market(s)

Any business

Industry/Entity Type

It Company

Requirements
Must have
• jQuery slider banner
Should not have
• Alter the logo in any way

```html
<!DOCTYPE html>
<html lang="en">
<head>
<meta charset="utf-8">
<title>Quillby Signs &amp; Digital Printing</title>
<link rel="stylesheet" href="https://fonts.googleapis.com/css2?family=Bitter:wght@700&family=Montserrat:wght@500;600&family=Metrophobic&display=swap">
<style>
:root{
  --yellow:#f5c43a;
  --yellow-deep:#efab24;
  --yellow-light:#fbd55a;
  --ink:#111111;
  --dark:#1f1f1f;
  --dark-2:#262626;
  --grey-text:#8c8c8c;
  --gold:#f2b632;
  --red:#d9382c;
  --red-deep:#b81f1b;
  --white:#ffffff;
  --field:#ddd6d0;
  --field-border:#c9c1ba;
  --panel:#eeeae6;
  --body-text:#555555;
  --frame:#6b6b6b;
}
*{box-sizing:border-box;margin:0;padding:0}
html,body{width:1048px;height:1200px;overflow:hidden}
body{position:relative;background:var(--white);font-family:"Metrophobic",sans-serif;color:var(--body-text)}
.abs{position:absolute}

/* header */
.top-strip{left:0;top:0;width:1048px;height:18px;background:var(--dark)}
.hero{left:0;top:18px;width:1048px;height:506px;background:radial-gradient(ellipse at 55% 40%,var(--yellow-light) 0%,var(--yellow) 55%,var(--yellow-deep) 100%)}
.nav-bar{left:0;top:18px;width:1048px;height:43px;background:linear-gradient(var(--gold),var(--yellow-deep));box-shadow:0 2px 4px rgba(0,0,0,.12)}
.brand{left:136px;top:14px;display:flex;align-items:center;gap:10px;font-family:"Bitter",serif;font-weight:700;font-size:40px;color:#4b2e86;line-height:1}
.brand-mark{width:18px;height:18px;background:#4b2e86;border-radius:50%}
.main-nav{right:118px;top:30px;display:flex;gap:28px;font-family:"Montserrat",sans-serif;font-weight:600;font-size:14px;color:var(--ink)}

/* hero */
.hero-title{left:137px;top:208px;font-family:"Bitter",serif;font-size:29px;color:var(--ink)}
.hero-copy{left:137px;top:247px;width:210px;font-family:"Montserrat",sans-serif;font-weight:500;font-size:11.5px;line-height:16.5px;color:var(--ink)}
.hero-visual{left:346px;top:147px;width:524px;height:320px;border-radius:4px;background:linear-gradient(90deg,#1d1d1d 0%,#1d1d1d 40%,#d9312f 46%,#d9312f 72%,#e9d74a 78%,#e9d74a 100%);opacity:.9}
.slider-arrows{left:146px;top:477px}

/* dark band */
.feature-band{left:0;top:524px;width:1048px;height:382px;background:var(--dark-2)}
.section-title{font-family:"Bitter",serif;font-size:20px;color:var(--gold)}
.welcome-title{left:124px;top:555px}
.welcome-copy{left:124px;top:589px;width:270px;font-size:11.5px;line-height:16.5px;color:var(--grey-text)}
.services-title{left:124px;top:739px}
.services-list{left:124px;top:779px;width:260px;display:grid;grid-template-columns:132px 128px;row-gap:8px;list-style:none;font-size:11.5px;line-height:15px;color:var(--grey-text)}
.services-list li{position:relative;padding-left:13px}
.services-list li::before{content:"\203A";position:absolute;left:3px;top:-1px;color:var(--grey-text)}
.gallery-title{left:410px;top:555px}
.gallery{left:410px;top:589px;display:grid;grid-template-columns:repeat(3,91px);grid-auto-rows:91px;gap:8px}
.gallery-thumb{border:4px solid var(--frame);background:linear-gradient(135deg,#f4f4f4,#bdbdbd)}
.thumb-dark{background:linear-gradient(135deg,#333,#777)}
.thumb-yellow{background:linear-gradient(135deg,#f1e15a,#c9b32f)}
.thumb-red{background:linear-gradient(135deg,#e0413a,#b4231f)}
.thumb-blue{background:radial-gradient(circle,#2d3f9a 55%,#f2f2f2 57%)}
.thumb-warn{background:linear-gradient(135deg,#f4f4f4,#e8c8c4)}

/* quote form */
.quote{left:723px;top:559px;width:204px;height:316px}
.quote-tab{left:0;top:0}
.quote-tab-label{left:10px;top:10px;font-family:"Montserrat",sans-serif;font-weight:600;font-size:13px;color:var(--white);letter-spacing:.3px}
.quote-panel{left:0;top:35px;width:204px;height:281px;background:var(--panel);border-radius:0 4px 4px 4px}
.field{left:9px;width:186px;height:29px;background:var(--field);border:1px solid var(--field-border);border-radius:4px;padding:7px 8px;font-size:11.5px;color:#555}
.field-message{height:74px}
.field-select::after{content:"";position:absolute;right:10px;top:11px;border:6px solid transparent;border-top:7px solid #8a8580}
.send-btn{left:9px;top:275px;width:59px;height:24px;border-radius:4px;background:linear-gradient(var(--red),var(--red-deep));color:var(--white);font-family:"Montserrat",sans-serif;font-weight:600;font-size:11.5px;text-align:center;line-height:24px}

/* locations */
.red-rule{left:0;top:906px;width:1048px;height:5px;background:var(--red)}
.locations-title{left:166px;top:924px;font-family:"Bitter",serif;font-size:20px;color:var(--red)}
.pin{left:124px;top:920px}
.store{top:973px;width:200px}
.store-name{font-family:"Montserrat",sans-serif;font-weight:500;font-size:14.5px;color:var(--ink);margin-bottom:10px}
.store-detail{font-size:11.5px;line-height:16.5px;color:#6e6e6e}
.store-detail p+p{margin-top:16px}
.divider{top:978px;width:1px;height:100px;background:#d8d8d8}
.hours{left:723px;top:968px;width:204px;height:109px;background:var(--red);border-radius:3px;padding:12px 15px;color:var(--white)}
.hours-title{font-family:"Bitter",serif;font-size:20px;margin-bottom:7px}
.hours-copy{font-size:11.5px;line-height:16.5px}

/* footer */
.grey-rule{left:0;top:1104px;width:1048px;height:5px;background:#cfcfcf}
.site-footer{left:0;top:1109px;width:1048px;height:91px;background:var(--dark)}
.footer-nav{left:122px;top:1133px;display:flex;gap:28px;font-family:"Montserrat",sans-serif;font-weight:500;font-size:13.5px;color:#e8e8e8}
.social{top:1131px;width:22px;height:22px;border-radius:2px}
.social-a{left:876px;background:#39a9dc}
.social-b{left:906px;background:#3b5998}
.copyright{left:122px;top:1171px;font-size:11px;color:#cfcfcf}
</style>
</head>
<body>

<div class="abs top-strip"></div>
<section class="abs hero"></section>
<header>
  <div class="abs nav-bar"></div>
  <div class="abs brand"><span class="brand-mark"></span>Quillby Signs</div>
  <nav class="abs main-nav"><span>Home</span><span>About Us</span><span>Our Services</span><span>Our Portfolio</span><span>Contact Us</span></nav>
</header>

<h1 class="abs hero-title">Sign Solutions</h1>
<p class="abs hero-copy">Quillby Signs will exceed customer expectations by offering a personalised approach to clients, embracing and executing individual needs through a comprehensive range of services.</p>
<div class="abs hero-visual" role="img" aria-label="Photo of three A-frame street signs: a black directional sign, a red salon sign and a yellow lunch bar sign"></div>
<svg class="abs slider-arrows" width="56" height="40" viewBox="0 0 56 40" aria-label="Slider controls">
  <polyline points="17,3 3,20 17,37" fill="none" stroke="#111" stroke-width="4"/>
  <polyline points="36,3 50,20 36,37" fill="none" stroke="#111" stroke-width="4"/>
</svg>

<section class="abs feature-band"></section>
<h2 class="abs section-title welcome-title">Welcome to Quillby</h2>
<p class="abs welcome-copy">Quillby Signs is a West Australian owned and managed company. We manufacture signage for any application; vinyl lettering, pull up banners, vehicle signage, in fact anything that requires our customers seeing the full picture when it comes to advertising their business. So if you're serious about the best, put us to the test!</p>
<h2 class="abs section-title services-title">Our Services</h2>
<ul class="abs services-list">
  <li>Quality Stickers &amp; Decals</li><li>Construction and safety Signs</li>
  <li>All Sign Types</li><li>Window Signage</li>
  <li>Vehicle Signage</li><li>Laminating</li>
  <li>Magnets</li>
</ul>

<h2 class="abs section-title gallery-title">Photo Gallery</h2>
<div class="abs gallery">
  <div class="gallery-thumb thumb-dark" role="img" aria-label="Black directional A-frame sign"></div>
  <div class="gallery-thumb thumb-yellow" role="img" aria-label="Yellow lunch bar A-frame sign"></div>
  <div class="gallery-thumb thumb-red" role="img" aria-label="Red salon A-frame sign"></div>
  <div class="gallery-thumb" role="img" aria-label="Lettering on a white truck panel"></div>
  <div class="gallery-thumb" role="img" aria-label="Signage on the tailgate of a white vehicle"></div>
  <div class="gallery-thumb" role="img" aria-label="Lettering on the back of a white ute"></div>
  <div class="gallery-thumb thumb-warn" role="img" aria-label="Red danger warning sign"></div>
  <div class="gallery-thumb thumb-warn" role="img" aria-label="Assorted safety and caution signs"></div>
  <div class="gallery-thumb thumb-blue" role="img" aria-label="Blue mandatory hard hat safety sign"></div>
</div>

<form class="abs quote">
  <svg class="abs quote-tab" width="204" height="36" viewBox="0 0 204 36"><path d="M0 36V6a6 6 0 0 1 6-6h120l22 26q5 10 18 10z" fill="#c8241f"/></svg>
  <span class="abs quote-tab-label">QUICK QUOTE</span>
  <div class="abs quote-panel"></div>
  <div class="abs field" style="top:45px">Name</div>
  <div class="abs field" style="top:82px">Email</div>
  <div class="abs field" style="top:119px">Phone</div>
  <div class="abs field field-select" style="top:156px">Slect Store</div>
  <div class="abs field field-message" style="top:192px">Message</div>
  <div class="abs send-btn">Send</div>
</form>

<div class="abs red-rule"></div>
<svg class="abs pin" width="36" height="36" viewBox="0 0 36 36" aria-hidden="true">
  <circle cx="18" cy="18" r="16" fill="none" stroke="#d9382c" stroke-width="4" stroke-dasharray="5 3"/>
  <path d="M18 8a7 7 0 0 0-7 7c0 5 7 12 7 12s7-7 7-12a7 7 0 0 0-7-7z" fill="#d9382c"/>
  <circle cx="18" cy="15" r="2.6" fill="#fff"/>
</svg>
<h2 class="abs locations-title">Store Locations</h2>

<div class="abs store" style="left:124px">
  <h3 class="store-name">Willetton</h3>
  <div class="store-detail"><p>Unit 3, 18-22 Marlow Avenue<br>Willetton, WA 6155</p><p>Phone: (08) 9000 1482<br>Fax: (08) 9000 1482</p></div>
</div>
<div class="abs divider" style="left:324px"></div>
<div class="abs store" style="left:352px">
  <h3 class="store-name">Joondalup</h3>
  <div class="store-detail"><p>Shop 7, 54 Fenton Promenade,<br>Joondalup,W.A</p><p>Phone: 08 9000 2716</p></div>
</div>
<div class="abs divider" style="left:540px"></div>
<div class="abs store" style="left:569px">
  <h3 class="store-name">South Lakes</h3>
  <div class="store-detail"><p>418 Harlan Lake Road<br>South Lake, WA</p><p>Phone: 08</p></div>
</div>
<div class="abs hours">
  <h3 class="hours-title">Trading Hours</h3>
  <p class="hours-copy">Monday – Friday<br>9:00am – 5:00pm<br>All other times by appointment</p>
</div>

<div class="abs grey-rule"></div>
<footer class="abs site-footer"></footer>
<nav class="abs footer-nav"><span>Home</span><span>About Us</span><span>Our Services</span><span>Our Portfolio</span><span>Contact Us</span></nav>
<span class="abs social social-a" role="img" aria-label="Social link"></span>
<span class="abs social social-b" role="img" aria-label="Social link"></span>
<p class="abs copyright">Copyright © 2013 Quillby. All rights reserved.</p>

</body>
</html>
```